high end contractor

high end contracting company we do all phases of construction kitchen,bathrooms,etc... please look at my website before you design www.harborkeybuild.com

would love some sort of lines or logo or both

Industry/Entity Type

Construction

Contact Information for Business Card

company name: oak & meridian contracting address: 318 fenwick st mount Vernon ny 10552 email: harborkeybuild@mailbrook.com website: www.harborkeybuild.com office#: 914-208-3916 fax#: 914-208-5523 dominic valtersen mobile# 917-526-0389

```html
<!DOCTYPE html>
<html lang="en">
<head>
<meta charset="utf-8">
<title>Oak &amp; Meridian Contracting — Business Card</title>
<link rel="stylesheet" href="https://fonts.googleapis.com/css2?family=Orbitron:wght@600;700&family=Michroma&display=swap">
<style>
  :root {
    --orange: #f07f21;
    --taupe: #8a7764;
    --ink: #4a4a4a;
    --paper: #ffffff;
    --backdrop: #202020;
  }
  * { box-sizing: border-box; margin: 0; padding: 0; }
  html, body { width: 1200px; height: 864px; overflow: hidden; }
  body { background: var(--backdrop); position: relative; font-family: "Michroma", sans-serif; }

  .card {
    position: absolute; top: 278px; width: 540px; height: 308px;
    background: var(--paper); overflow: hidden;
    box-shadow: 0 10px 30px rgba(0,0,0,.45);
  }
  .card--front { left: 40px; }
  .card--back { left: 620px; }

  .brand { position: absolute; display: flex; align-items: center; gap: 10px; }
  .brand__mark { width: 16px; height: 16px; background: var(--orange); flex: none; }
  .brand__name {
    font-family: "Orbitron", sans-serif; font-weight: 700; color: var(--orange);
    text-transform: uppercase; letter-spacing: .5px; line-height: 1.15;
  }
  .card--front .brand { left: 0; right: 0; top: 120px; justify-content: center; }
  .card--front .brand__name { font-size: 21px; }
  .card--back .brand { right: 26px; top: 88px; }
  .card--back .brand__name { font-size: 15px; }

  .band { position: absolute; left: 0; top: 0; width: 540px; height: 308px; }

  .person { position: absolute; left: 30px; top: 112px; }
  .person__name {
    font-family: "Orbitron", sans-serif; font-weight: 600; font-size: 18px;
    color: var(--orange); text-transform: uppercase; letter-spacing: .5px;
  }
  .person__role { font-size: 8px; color: var(--ink); text-transform: uppercase; margin-top: 4px; letter-spacing: .5px; }

  .contacts { position: absolute; left: 30px; top: 162px; list-style: none; }
  .contacts li { display: flex; align-items: center; gap: 8px; font-size: 7.5px; color: var(--ink); height: 17px; }
  .contacts svg { width: 10px; height: 10px; fill: var(--orange); flex: none; }

  .address {
    position: absolute; left: 270px; top: 256px; width: 250px;
    font-size: 8px; color: var(--paper); text-align: center; letter-spacing: .3px;
  }
</style>
</head>
<body>
  <section class="card card--front" aria-label="Card front">
    <div class="brand">
      <span class="brand__mark"></span>
      <span class="brand__name">Oak &amp; Meridian<br>Contracting</span>
    </div>
  </section>

  <section class="card card--back" aria-label="Card back">
    <svg class="band" viewBox="0 0 540 308" aria-hidden="true">
      <path d="M0 292 H200 C228 292 222 242 250 242 H540 V308 H0 Z" fill="var(--orange)"/>
      <path d="M0 283 H194 C220 283 214 232 244 232 H540" fill="none" stroke="var(--taupe)" stroke-width="4"/>
    </svg>

    <div class="brand">
      <span class="brand__mark"></span>
      <span class="brand__name">Oak &amp; Meridian<br>Contracting</span>
    </div>

    <div class="person">
      <p class="person__name">Dominic Valtersen</p>
      <p class="person__role">Owner</p>
    </div>

    <ul class="contacts">
      <li><svg viewBox="0 0 10 10"><rect x="2.5" y="0" width="5" height="10" rx="1"/></svg>917-526-0389</li>
      <li><svg viewBox="0 0 10 10"><path d="M2 0 L4 2.5 L3 4 Q4.5 6.5 6 7 L7.5 6 L10 8 L8.5 10 Q3 9.5 0 2 Z"/></svg>914-208-3916</li>
      <li><svg viewBox="0 0 10 10"><rect x="0" y="3" width="10" height="6" rx="1"/><rect x="2" y="0" width="6" height="3"/></svg>914-208-5523</li>
      <li><svg viewBox="0 0 10 10"><path d="M0 2 H10 V8 H0 Z"/><path d="M0 2 L5 6 L10 2" stroke="#fff" stroke-width="1" fill="none"/></svg>harborkeybuild@mailbrook.com</li>
      <li><svg viewBox="0 0 10 10"><circle cx="5" cy="5" r="5"/><path d="M0 5 H10 M5 0 V10" stroke="#fff" stroke-width=".8"/></svg>www.harborkeybuild.com</li>
    </ul>

    <p class="address">318 Fenwick St, Mount Vernon NY 10552</p>
  </section>
</body>
</html>
```